Pharmaceutical Manufacturing Services Advertisement

We need a new full page advertisement designed for publication in international magazines. We are a custom pharmaceutical manufacturing company and we help biotechnology companies scale up their drug development for clinical trials. The products we help manufacture are therapeutics for global healthcare problems.

Target Market(s)

Verott Bio is a privately owned contract development manufacturing organisation (CDMO) headquartered in Darra, QLD, Australia.

Our mission is to is to be a global leader in development and in the provision of contract manufacturing for active pharmaceutical ingredient processes.

Why we do what we Do:

To help advance Biotechnology Companies so that they can deliver innovative therapeutics
~ enabling patients to live longer, healthier and happier lives
~ which solves worldwide health problems

Verott Bio’s role is to develop, implement and scale up the production to deliver biologic medicines for patients in partnership with the biotechnology companies.

Industry/Entity Type

Biotechnology

Font styles to use
Sans Serif

Colors

Designer to choose colors to be used in the design.

Requirements
Must have
• Please see the script on the Word document. There are 4 optional Header Taglines. Additional ideas for multiple designs for the taglines welcomed.
• However preference is for either of the first two:
• 1. Building your vision for better healthcare
• 2. Bridging your vision for better healthcare
• File Specs:
• • All artwork should be submitted as high-resolution (300 min. dpi), press-ready PDF files
• • CMYK color only
• • Full page 8.25” x 10.812”; 209.55 x 274.62 mm
• • Live Area for all sizes: 0.25” (6.35 mm) inside the trim
• • Bleed Area for all sizes: Extends 0.125” (3.175 mm) from trim
Nice to have
• Modern Science look to inspire biotechnology companies to work with us.
• Search for images to use by keyword "recombinant dna"

```html
<!DOCTYPE html>
<html lang="en">
<head>
<meta charset="utf-8">
<title>Verott Bio – Building Your Vision for Better Healthcare</title>
<link rel="stylesheet" href="https://fonts.googleapis.com/css2?family=Montserrat:wght@600;800;900&family=Raleway:wght@300;400&family=Roboto+Condensed:wght@400&display=swap">
<style>
  :root{
    --navy:#013e5e;
    --green:#afbf38;
    --grey:#bdbdbd;
    --logo-grey:#5a6470;
    --white:#ffffff;
    --stage:#231f20;
    --photo-teal:#1f6f82;
    --photo-deep:#0f3f52;
    --photo-gold:#c9b45a;
  }
  *{margin:0;padding:0;box-sizing:border-box}
  html,body{width:1200px;height:1200px;overflow:hidden;background:var(--stage)}
  .page{
    position:absolute;left:136px;top:0;
    width:1310px;height:1695px;
    transform:scale(0.70796);transform-origin:0 0;
    background:var(--navy);overflow:hidden;
    font-family:'Raleway',sans-serif;color:var(--white);
  }
  .page svg{position:absolute;left:0;top:0}
  .headline{position:absolute;left:102px;top:720px;line-height:1}
  .headline .light{display:block;font-family:'Raleway',sans-serif;font-weight:300;font-size:58px;letter-spacing:0.5px}
  .headline .strong{display:block;font-family:'Montserrat',sans-serif;font-weight:900;font-size:52px;color:var(--green);line-height:48px;margin-top:4px}
  .subline{position:absolute;left:102px;top:882px;font-family:'Raleway',sans-serif;font-weight:400;font-size:29px;line-height:31px;letter-spacing:0.3px}
  .intro{position:absolute;left:721px;top:542px;width:520px;font-weight:300;font-size:25.5px;line-height:34.5px}
  .intro p+p{margin-top:34.5px}
  .intro .accent{color:var(--green);font-weight:400}
  .offer{position:absolute;left:140px;top:1145px;color:var(--navy);font-family:'Montserrat',sans-serif}
  .offer h2{font-weight:800;font-size:31px;letter-spacing:0.3px;margin-bottom:12px}
  .offer ul{list-style:none;font-weight:600;font-size:24.5px;line-height:34.5px}
  .offer li{position:relative;padding-left:21px}
  .offer li::before{content:"•";position:absolute;left:0}
  .offer ul+h2{margin-top:45px}
  .brand{position:absolute;left:700px;top:1318px;width:510px;text-align:center}
  .brand .name{font-family:'Montserrat',sans-serif;font-weight:600;font-size:92px;line-height:1;color:var(--navy);letter-spacing:1px}
  .brand .tagline{font-family:'Roboto Condensed',sans-serif;font-weight:400;font-size:31px;color:var(--logo-grey);margin-top:12px;letter-spacing:-0.3px}
  .phone{position:absolute;left:663px;top:1500px;width:573px;height:57px;border-radius:28px;background:var(--navy);color:var(--white);font-family:'Montserrat',sans-serif;font-weight:800;font-size:35px;line-height:57px;text-align:center;letter-spacing:0.5px}
  .contact{position:absolute;left:663px;top:1572px;width:573px;text-align:center;font-family:'Montserrat',sans-serif;font-weight:600;font-size:23px;line-height:35px;color:var(--navy)}
  .contact .icon{display:inline-block;vertical-align:-3px;margin-right:6px}
</style>
</head>
<body>
  <main class="page">
    <svg class="backdrop" width="1310" height="1695" viewBox="0 0 1310 1695" aria-hidden="true">
      <polygon points="0,472 328,594 0,717" fill="var(--grey)"/>
      <polygon points="0,1542 1310,1048 1310,1695 0,1695" fill="var(--white)"/>
      <polygon points="1140,1112 1310,1048 1310,1200" fill="var(--grey)"/>
      <polygon points="102,1087 570,935 570,1695 102,1695" fill="var(--green)"/>
    </svg>

    <svg class="hero-photo" width="1310" height="600" viewBox="0 0 1310 600" role="img" aria-label="Photo of a lab technician in a hairnet and safety glasses beside filtration cartridges in a biomanufacturing cleanroom">
      <defs>
        <linearGradient id="heroTone" x1="0" y1="0" x2="1" y2="0">
          <stop offset="0" stop-color="var(--photo-gold)"/>
          <stop offset="0.35" stop-color="var(--photo-teal)"/>
          <stop offset="1" stop-color="var(--photo-deep)"/>
        </linearGradient>
      </defs>
      <polygon points="0,0 1310,0 1310,225 328,594 0,472" fill="url(#heroTone)"/>
    </svg>

    <h1 class="headline">
      <span class="light">BUILDING YOUR</span>
      <span class="strong">VISION FOR BETTER</span>
      <span class="strong">HEALTHCARE</span>
    </h1>
    <p class="subline">Your Partner in Early Phase Clinical<br>Biomanufacturing</p>

    <div class="intro">
      <p>We have been serving the pharmaceutical, biotechnology and veterinary industry for over <span class="accent">20 years</span> so you can create innovative medicines for worldwide health problems.</p>
      <p>Get your therapeutics to the patient faster with cost-effective manufacturing for your GMP clinical trial material. We offer rapid technology transfer, scale-up development and manufacturing of microbial cell-derived proteins at up to 500L scale. We prepare your active pharmaceutical ingredient (API) products to a world class standard ready for clinical development.</p>
    </div>

    <section class="offer">
      <h2>PRODUCTS:</h2>
      <ul>
        <li>Recombinant proteins</li>
        <li>Live Biotherapeutics</li>
        <li>Bacterial vaccines</li>
        <li>Plasmid DNA</li>
      </ul>
      <h2>SERVICES:</h2>
      <ul>
        <li>Bacterial / Yeast Fermentation</li>
        <li>Cell Banking</li>
        <li>Process Development/Scale-up</li>
        <li>cGMP Manufacture of<br>biopharmaceutical APIs</li>
        <li>Stability Testing</li>
      </ul>
    </section>

    <div class="brand">
      <div class="name">VEROTT BIO</div>
      <div class="tagline">BIOPHARMACEUTICAL MANUFACTURING</div>
    </div>

    <div class="phone">AUSTRALIA +61(7)35550142</div>
    <div class="contact">
      <div><svg class="icon" style="position:static" width="20" height="18" viewBox="0 0 20 18" aria-hidden="true"><rect x="1" y="3" width="18" height="13" fill="none" stroke="var(--navy)" stroke-width="2"/><polyline points="1,3 10,10 19,3" fill="none" stroke="var(--navy)" stroke-width="2"/></svg>enquiries@verottbio.com.au</div>
      <div><svg class="icon" style="position:static" width="20" height="20" viewBox="0 0 20 20" aria-hidden="true"><circle cx="10" cy="10" r="8.5" fill="none" stroke="var(--navy)" stroke-width="1.8"/><ellipse cx="10" cy="10" rx="3.8" ry="8.5" fill="none" stroke="var(--navy)" stroke-width="1.5"/><line x1="1.5" y1="10" x2="18.5" y2="10" stroke="var(--navy)" stroke-width="1.5"/></svg>www.verottbio.com.au</div>
    </div>
  </main>
</body>
</html>
```